Nera Bloom Fitness Coaching Project

I am a personal trainer based in London. My services include one-on-one PT sessions, bootcamps.
I would like the design to be minimalistic. With light colours: white, pink, purple.
I specialise in weight loss, flexibility, mobility.

Orla Pemvick
Personal Trainer
Email: orla.pemvick@tovamail.com
tel: 07400918243
Instagram: Nera Bloom

Target Market(s)

adults, mostly females (age 18-50).

Industry/Entity Type

Fitness

Contact Information for Business Card

Orla Pemvick
Personal Trainer
tel: 07400918243
Instagram: Nera Bloom

Font styles to use
Serif

Colors
eea4c8
fbd4d5
fdf9cf
cfeae6
cee9f5

Requirements
Nice to have
• minimalistic style
• easy to read and remember

```html
<!DOCTYPE html>
<html lang="en">
<head>
<meta charset="utf-8">
<title>Orla Pemvick – Business Card</title>
<link href="https://fonts.googleapis.com/css2?family=Jost:wght@400;500&display=swap" rel="stylesheet">
<style>
  :root {
    --backdrop: #3b3b3d;
    --card-white: #ffffff;
    --cream-frame: #fdf9cf;
    --photo-dark: #0d0c0b;
    --photo-warm: #5a3a24;
    --pink: #eb9fc7;
    --name-light: #fbf7ee;
  }
  * { margin: 0; padding: 0; box-sizing: border-box; }
  html, body {
    width: 1200px; height: 859px; overflow: hidden;
    background: var(--backdrop);
    font-family: "Jost", "Futura", sans-serif;
  }
  .stage {
    position: relative; width: 1200px; height: 859px;
  }
  .card {
    position: absolute; left: 310px; width: 580px; height: 332px;
    box-shadow: 0 10px 28px rgba(0,0,0,.45);
  }
  /* Front */
  .card-front {
    top: 70px;
    background: var(--cream-frame);
    padding: 11px;
  }
  .front-photo {
    position: relative; width: 100%; height: 100%;
    background:
      radial-gradient(ellipse 30% 48% at 52% 52%, var(--photo-warm) 0%, rgba(60,38,22,.6) 55%, transparent 100%),
      radial-gradient(ellipse 22% 30% at 78% 58%, rgba(120,80,80,.35), transparent 100%),
      var(--photo-dark);
  }
  .front-name {
    position: absolute; left: 0; right: 0; top: 50%;
    transform: translateY(-50%);
    text-align: center;
    color: var(--name-light);
    font-size: 31px; font-weight: 400;
    letter-spacing: .24em;
  }
  /* Back */
  .card-back {
    top: 458px;
    background: var(--card-white);
    color: var(--pink);
  }
  .back-title-name {
    position: absolute; right: 40px; top: 34px;
    font-size: 29px; letter-spacing: .2em; font-weight: 400;
  }
  .divider-long {
    position: absolute; left: 40px; right: 40px; top: 176px;
    height: 1px; background: var(--pink);
  }
  .social {
    position: absolute; right: 40px; top: 190px;
    display: flex; align-items: center; gap: 8px;
    font-size: 13px; letter-spacing: .16em;
  }
  .social-square {
    width: 10px; height: 10px; background: var(--pink);
  }
  .contact-block {
    position: absolute; left: 40px; top: 196px; width: 330px;
  }
  .person-name {
    font-size: 23px; font-weight: 500; letter-spacing: .16em;
  }
  .person-role {
    font-size: 13px; letter-spacing: .18em; margin-top: 2px;
  }
  .divider-short {
    height: 1px; background: var(--pink); width: 200px; margin: 12px 0 10px;
  }
  .contact-line {
    display: flex; align-items: center; gap: 9px;
    font-size: 15px; letter-spacing: .16em; line-height: 24px;
  }
  .contact-line svg { width: 12px; height: 12px; flex: none; }
</style>
</head>
<body>
  <main class="stage">
    <section class="card card-front">
      <div class="front-photo" role="img" aria-label="Portrait photograph of the personal trainer against a dark background">
        <h1 class="front-name">ORLA PEMVICK</h1>
      </div>
    </section>

    <section class="card card-back">
      <p class="back-title-name">ORLA PEMVICK</p>
      <div class="divider-long"></div>
      <p class="social"><span class="social-square"></span>Nera Bloom</p>
      <div class="contact-block">
        <p class="person-name">Orla Pemvick</p>
        <p class="person-role">Personal Trainer</p>
        <div class="divider-short"></div>
        <p class="contact-line">
          <svg viewBox="0 0 12 12" aria-hidden="true"><path d="M2.5 1 L4.5 1 L5.2 3.6 L4 4.6 Q5 7 7.4 8 L8.4 6.8 L11 7.5 L11 9.5 Q11 11 9.5 11 Q1 10.5 1 2.5 Q1 1 2.5 1 Z" fill="#eb9fc7"/></svg>
          07400918243
        </p>
        <p class="contact-line">
          <svg viewBox="0 0 12 12" aria-hidden="true"><rect x="1" y="2.5" width="10" height="7" fill="none" stroke="#eb9fc7" stroke-width="1.2"/><path d="M1 2.5 L6 6.5 L11 2.5" fill="none" stroke="#eb9fc7" stroke-width="1.2"/></svg>
          orla.pemvick@tovamail.com
        </p>
      </div>
    </section>
  </main>
</body>
</html>
```